Premium Lawn fertiliser packaging - Looking for long term designer

*Update at bottom
I need a carefully considered, bold and professional packaging design for my new premium lawn fertiliser product. This contest is for a detailed front of the stand-up pouch packaging and once I’ve chosen a winner, they’ll be asked to create the layout for the back that links to the front as well. I have a full range of additional products that will also need designs and so I'm looking for someone who can do a great job here and who we can work with long term.

The front should include our logo for Pemberly Turf Supply Direct and be titled “Bloom Vigor Max” "Professional Lawn Fertiliser". The spring fertiliser tag line is "Awaken your lawn: Lush Greening, Lasting Health".
Beneath it, it then needs to include some important usage information and the key benefits along with some suitable graphic.

Key information to include:

Apply March - June
Treats 35-50 m2
16-3-8
+2%MgO + 1% Fe + 2.9% CaO (this is the chemical makeup of the fertiliser and needs to be fairly prominent. If you look at other professional fertiliser packaging, you'll see how it needs to compare).

Key features:
Premium fertiliser, used by professionals
Advanced greening with micro-nutrient complex
Dual action Nitrogen: Instant green boost & continuous feed for 3 months
Child & pet safe

Our brand colours are purple and green. Purple = #592999, Green = 3cb64a / 81d742 / 4d9d44

I think these colours look great against a white background.

Please make sure you look at our website as well to get an idea of our brand: www.pemberlyturfsupply.co.uk

To help, I've attached images of competitors fertiliser packaging that I like the look of. I'm not looking for you to copy but just see what type of thing appeals to me, the standard I'm expecting and what I need to compete against....

In addition, I have also attached some potential images you may wish to try using in your design, although please feel free to use your own if you have something better. For the moment, the images are 'preview' images, but once I decide on a design and we agree on the correct image, I will download and send over a fully licensed version.

*** Update*** When submitting your design, can you submit it in 2 formats: The first as a fully printed custom stand-up pouch and the second as a full-size label stuck onto a standup pouch (whatever colour you think is right for your design - choose white if you are not sure). To explain, I've just discovered we won't be able to get full custom bags printed in time for the first run and so we will have to opt for the design to be printed on labels and fixed onto bags. I therefore need to choose a design that works in both formats as both a label on a standup pouch as well as a fully printed pouch. Many thanks.

Target Market(s)

Domestic home-owners

Industry/Entity Type

Lawn care. NOT AGRICULTURE OR FARMING

Font styles to use
Sans Serif

Requirements
Must have
• Presented in 2 formats - see update at bottom of description
Nice to have
• I quite like designs against a white background, although I’m open to other ideas as well.
Should not have
• Please do not include any people or faces in the design. The text should be solid in colour, so no graduated colour fill in the text or outline text. Please avoid over-busy or cluttered designs.

```html
<!DOCTYPE html>
<html lang="en">
<head>
<meta charset="utf-8">
<title>Bloom Vigor Max – Pouch Front</title>
<link href="https://fonts.googleapis.com/css2?family=Cinzel:wght@700;900&family=Open+Sans:ital,wght@0,600;0,700;1,600&family=Oswald:wght@300;400;500&display=swap" rel="stylesheet">
<style>
  :root{
    --purple:#592999;
    --purple-bright:#8a1fd0;
    --purple-deep:#5b1fb0;
    --green:#3cb64a;
    --green-light:#81d742;
    --green-dark:#4d9d44;
    --brown:#3b2a1f;
    --gold:#c9963a;
    --gold-light:#f2cf7a;
    --ink:#1d1d1d;
    --white:#ffffff;
    --backdrop:#f3f3f3;
  }
  *{margin:0;padding:0;box-sizing:border-box}
  html,body{width:1200px;height:976px;overflow:hidden;background:var(--backdrop)}
  .canvas{position:relative;width:1200px;height:976px;display:flex;align-items:center;justify-content:center}
  .pouch{position:relative;width:560px;height:940px;border-radius:14px;overflow:hidden;box-shadow:0 6px 24px rgba(0,0,0,.12)}
  .pouch-art{position:absolute;inset:0}
  .brand{position:absolute;top:150px;left:0;width:440px;display:flex;align-items:center;justify-content:center;gap:10px}
  .brand-dot{width:22px;height:22px;border-radius:50%;background:var(--green)}
  .brand-name{font:700 23px/1.1 "Open Sans",sans-serif;color:var(--brown);text-align:center}
  .title{position:absolute;left:0;width:560px;text-align:center;font-family:"Cinzel",serif;font-weight:900;color:var(--purple-bright);letter-spacing:1px}
  .title-top{top:232px;font-size:86px;line-height:1}
  .title-bottom{top:330px;font-size:62px;line-height:1}
  .pill{position:absolute;top:420px;left:56px;width:428px;height:38px;border-radius:19px;background:var(--green);color:var(--white);font:600 19px/38px "Open Sans",sans-serif;text-align:center;letter-spacing:.5px}
  .tagline{position:absolute;top:468px;left:0;width:560px;text-align:center;font:italic 600 17px/1.2 "Open Sans",sans-serif;color:var(--ink)}
  .tagline span{margin-left:14px}
  .badge{position:absolute;left:398px;top:100px;width:120px;height:120px;display:flex;flex-direction:column;align-items:center;justify-content:center;font-family:"Oswald",sans-serif;color:var(--white);text-align:center}
  .badge-apply{font-size:23px;font-weight:500;line-height:1}
  .badge-months{font-size:14px;font-weight:500;line-height:1;margin:6px 0 5px;padding:4px 0;border-top:1px solid var(--gold);border-bottom:1px solid var(--gold)}
  .badge-year{font-size:24px;font-weight:500;line-height:1;color:var(--gold-light)}
  .usage{position:absolute;left:36px;top:742px;color:var(--white);font-family:"Oswald",sans-serif}
  .coverage{font-size:30px;font-weight:500;line-height:1}
  .formula{font-size:21px;font-weight:400;margin-top:10px;line-height:1}
  .features{list-style:none;margin-top:14px}
  .features li{font-size:13.5px;font-weight:300;line-height:1.95;display:flex;align-items:center;gap:8px}
  .features svg{width:11px;height:11px;flex:none}
  .net-weight{position:absolute;right:30px;top:900px;color:var(--white);font:400 18px/1 "Oswald",sans-serif}
</style>
</head>
<body>
<main class="canvas">
  <article class="pouch">
    <svg class="pouch-art" viewBox="0 0 560 940" width="560" height="940">
      <defs>
        <linearGradient id="pouchPurple" x1="0" y1="0" x2="1" y2="1">
          <stop offset="0" stop-color="#6a1fc0"/>
          <stop offset="1" stop-color="#9a1fd2"/>
        </linearGradient>
        <linearGradient id="sceneFill" x1="0" y1="0" x2="0" y2="1">
          <stop offset="0" stop-color="#ffffff"/>
          <stop offset="0.35" stop-color="#d8eaf7"/>
          <stop offset="0.62" stop-color="#cfe0ea"/>
          <stop offset="0.72" stop-color="#58803f"/>
          <stop offset="0.85" stop-color="#5ca82f"/>
          <stop offset="1" stop-color="#4e9a27"/>
        </linearGradient>
        <linearGradient id="ribbonGold" x1="0" y1="0" x2="1" y2="0">
          <stop offset="0" stop-color="#8a5a1c"/>
          <stop offset="0.5" stop-color="#e8b75a"/>
          <stop offset="1" stop-color="#8a5a1c"/>
        </linearGradient>
      </defs>
      <rect width="560" height="940" fill="url(#pouchPurple)"/>
      <path d="M0,58 C180,40 380,40 470,78 C530,105 556,170 560,250 L560,300 C548,205 505,150 440,128 C330,100 170,110 0,108 Z" fill="var(--green)"/>
      <path d="M0,128 C180,112 360,100 450,122 C520,142 556,200 560,290 L560,760 L0,760 Z" fill="var(--white)"/>
      <rect role="img" aria-label="Photograph of a suburban bungalow with porch, shrubs, conifers and a lush green lawn under a pale blue sky" x="0" y="250" width="560" height="520" fill="url(#sceneFill)"/>
      <path d="M0,676 C150,676 290,740 390,790 C470,830 530,820 560,800 L560,940 L0,940 Z" fill="var(--green)"/>
      <path d="M0,692 C150,692 285,755 385,803 C465,842 528,832 560,814 L560,940 L0,940 Z" fill="var(--white)"/>
      <path d="M0,698 C150,698 282,760 382,808 C462,847 528,838 560,820 L560,940 L0,940 Z" fill="url(#pouchPurple)"/>
      <rect x="432" y="0" width="52" height="120" fill="url(#ribbonGold)"/>
      <circle cx="458" cy="160" r="62" fill="var(--gold)"/>
      <circle cx="458" cy="160" r="56" fill="#141414"/>
      <circle cx="458" cy="160" r="51" fill="none" stroke="var(--gold)" stroke-width="1" stroke-dasharray="2 2"/>
    </svg>

    <div class="brand">
      <span class="brand-dot"></span>
      <span class="brand-name">Pemberly Turf<br>Supply Direct</span>
    </div>

    <div class="badge">
      <span class="badge-apply">APPLY</span>
      <span class="badge-months">MARCH - JUNE</span>
      <span class="badge-year">2024</span>
    </div>

    <h1 class="title title-top">BLOOM</h1>
    <p class="title title-bottom">VIGOR MAX</p>
    <p class="pill">PROFESSIONAL LAWN FERTILISER</p>
    <p class="tagline">Awaken your lawn:<span>Lush Greening, Lasting Health</span></p>

    <section class="usage">
      <p class="coverage">TREATS 35-50 M2</p>
      <p class="formula">16-3-8 +2%MGO + 1% FE + 2.9% CAO</p>
      <ul class="features">
        <li><svg viewBox="0 0 12 12"><path d="M1,6 L4.5,10 L11,1" fill="none" stroke="#fff" stroke-width="1.8"/></svg>Premium fertiliser, used by professionals</li>
        <li><svg viewBox="0 0 12 12"><path d="M1,6 L4.5,10 L11,1" fill="none" stroke="#fff" stroke-width="1.8"/></svg>Advanced greening with micro-nutrient complex</li>
        <li><svg viewBox="0 0 12 12"><path d="M1,6 L4.5,10 L11,1" fill="none" stroke="#fff" stroke-width="1.8"/></svg>Dual action Nitrogen: Instant green boost &amp; continuous feed for 3 months</li>
        <li><svg viewBox="0 0 12 12"><path d="M1,6 L4.5,10 L11,1" fill="none" stroke="#fff" stroke-width="1.8"/></svg>Child &amp; pet safe</li>
      </ul>
    </section>
    <p class="net-weight">NET WT. 25 LBS.</p>
  </article>
</main>
</body>
</html>
```